Website for Bramblewood Quarry Advisors

Please design a website that initially contains four or five pages. This work is for a newly formed consulting company, Bramblewood Quarry Advisors, that provides training and individual coaching to help business professionals and lawyers write more effectively and efficiently.

We work in a professional and conservative industry. The website should be simple, crisp, and clean.

I have attached a document that describes the four initial pages for the site: 1) a landing page, 2) a webpage that includes the pictures and bios of our two consultants, 3) a webpage that describes our services, and 4) a webpage that will contain a form that visitors can use to submit questions to us.

I also included the following files:
a. a powerpoint slide with our consultants' pictures and bios; and
b. our recently designed logo (jpg and png files).

Thank you!

```html
<!DOCTYPE html>
<html lang="en">
<head>
<meta charset="utf-8">
<title>Bramblewood Quarry Advisors</title>
<link rel="stylesheet" href="https://fonts.googleapis.com/css2?family=Poppins:wght@400;500;600;700;800&family=Tinos:wght@400;700&display=swap">
<style>
:root{
  --red:#c8232d;
  --red-soft:rgba(205,45,58,.82);
  --ink:#222;
  --text:#333;
  --muted:#555;
  --grey-bg:#f4f4f4;
  --ornament:#ececec;
  --field:#fff;
  --line:#e3e3e3;
  --serif:"Tinos", "Times New Roman", serif;
  --sans:"Poppins", Arial, sans-serif;
}
*{box-sizing:border-box;margin:0;padding:0}
html,body{width:1200px;height:5314px;overflow:hidden}
body{font-family:var(--sans);color:var(--text);background:#fff;position:relative}
.section{position:absolute;left:0;width:1200px}
.abs{position:absolute}

/* header */
.site-header{top:0;height:136px;background:#fff}
.brand{font-family:var(--serif);color:var(--ink);font-size:24px;left:78px;top:46px;white-space:nowrap}
.main-nav{right:76px;top:52px;display:flex;gap:48px;font-size:14px}
.main-nav a{color:var(--ink);text-decoration:none}
.main-nav a.active{color:var(--red)}

/* hero */
.hero{top:136px;height:837px}
.hero-photo{position:absolute;inset:0;background:linear-gradient(100deg,#3b3a3c 0%,#8a7a6b 30%,#c9b9a4 55%,#9e9790 80%,#6d6a67 100%)}
.hero-box{left:540px;top:169px;width:602px;height:443px;background:var(--red-soft);border-radius:40px;display:flex;align-items:center;justify-content:center;text-align:center}
.hero-box h1{font-family:var(--sans);font-weight:800;font-size:42px;line-height:64px;color:#fff;text-transform:uppercase;text-shadow:0 3px 6px rgba(0,0,0,.35)}

/* about */
.about{top:973px;height:703px}
.about h2{font-family:var(--serif);font-weight:400;font-size:36px;left:85px;top:118px;color:var(--ink)}
.about-copy{left:84px;top:232px;width:510px;font-size:13px;line-height:22.5px;color:var(--text)}
.about-copy p+p{margin-top:22px}
.btn{display:inline-flex;align-items:center;justify-content:center;border-radius:40px;font-family:var(--sans);font-weight:500;text-decoration:none}
.btn-red{background:var(--red);color:#fff}
.btn-white{background:#fff;color:var(--ink)}
.about .btn{left:74px;top:528px;width:180px;height:66px;font-size:14px}
.about-photo{left:621px;top:91px;width:524px;height:524px;border-radius:50%;background:linear-gradient(135deg,#d9b98f 0%,#e8e4da 40%,#9aa08f 70%,#2f3437 100%)}
.accent-dot{left:705px;top:17px;width:78px;height:78px;border-radius:50%;background:#fbe3e6}
.ornament{left:1037px;top:557px;width:84px;height:84px;border-radius:50%;background:var(--ornament)}

/* consultants */
.consultants{top:1676px;height:1031px;background:var(--grey-bg)}
.section-title{font-family:var(--serif);font-weight:700;color:var(--ink)}
.consultants h2,.services h2,.contact h2{position:absolute;left:0;width:100%;text-align:center;font-size:46px}
.consultants h2{top:96px}
.card{left:78px;width:1038px;border:3px solid var(--red);border-radius:26px;overflow:hidden;background:#fff;display:flex}
.card-one{top:204px;height:343px}
.card-two{top:576px;height:340px}
.card-profile{position:relative;width:339px;height:100%;background:#fff}
.card-two .card-profile{width:337px}
.card-bio{position:relative;flex:1;background:var(--red);color:#fff;font-size:12.3px;line-height:22.4px}
.portrait{position:absolute;left:72px;top:58px;width:194px;height:194px;border-radius:50%;background:linear-gradient(160deg,#8a8f96,#d9b79a 55%,#3a4a66)}
.card-two .portrait{left:80px;top:46px;background:linear-gradient(160deg,#6c6a6a,#7a5642 55%,#b23a3a)}
.person{position:absolute;left:0;width:100%;top:270px;text-align:center;color:var(--red);font-weight:600;font-size:26px}
.card-two .person{top:268px}
.card-one .card-bio p{position:absolute;left:36px;top:44px;width:620px}
.card-two .card-bio p{position:absolute;left:46px;top:44px;width:610px}
.card-bio .btn{position:absolute;width:161px;height:54px;font-size:14px}
.card-one .card-bio .btn{left:46px;top:254px}
.card-two .card-bio .btn{left:46px;top:256px}

/* services */
.services{top:2707px;height:1576px;background:#fff}
.services h2{top:86px}
.services-intro{top:178px;left:0;width:100%;text-align:center;font-size:13px;line-height:23px;color:var(--text)}
.service{width:415px;border-radius:26px;background:#fff;box-shadow:0 4px 14px rgba(0,0,0,.12);overflow:hidden;display:flex;flex-direction:column;align-items:center;text-align:center;padding-bottom:31px}
.service .shot{width:100%;flex:none}
.service h3{font-weight:400;color:var(--red);font-size:23px;line-height:23px;margin-top:42px;padding:0 30px}
.service p{font-size:13px;line-height:22px;color:var(--muted);margin-top:18px;padding:0 60px}
.service .btn{margin-top:auto;width:124px;height:41px;font-size:12px}
.s1{left:169px;top:289px;height:561px}
.s2{left:625px;top:289px;height:561px}
.s3{left:169px;top:906px;height:558px}
.s4{left:625px;top:906px;height:558px}

/* contact */
.contact{top:4283px;height:728px;background:var(--grey-bg)}
.contact-band{left:0;top:0;width:270px;height:728px;background:var(--red)}
.contact h2{top:92px;left:270px;width:924px;font-size:48px}
.contact-photo{left:57px;top:212px;width:384px;height:384px;border-radius:50%;border:4px solid var(--red);padding:7px;background:var(--grey-bg)}
.contact-photo div{width:100%;height:100%;border-radius:50%;background:linear-gradient(135deg,#cfc7bb 0%,#8f8678 45%,#2c2b2a 100%)}
.field{background:var(--field);border:1px solid var(--line);font-family:var(--sans);font-size:13px;color:#888;padding:0 20px;display:flex;align-items:center;height:46px}
.f-company{left:497px;top:235px;width:247px}
.f-contact{left:765px;top:235px;width:247px}
.f-phone{left:497px;top:301px;width:247px}
.f-email{left:765px;top:301px;width:247px}
.f-address{left:497px;top:369px;width:515px}
.f-message{left:497px;top:429px;width:515px;height:103px;align-items:flex-start;padding-top:14px}
.contact .btn{left:676px;top:575px;width:165px;height:50px;font-size:16px}

/* footer */
.site-footer{top:5011px;height:303px;background:#fff}
.footer-brand{left:0;width:100%;top:60px;text-align:center;font-family:var(--serif);font-size:31px;color:var(--ink)}
.dotted{left:78px;width:1046px;border-top:2px dotted var(--red)}
.footer-contact{top:178px;left:0;width:100%;height:44px}
.fc-item{position:absolute;top:0;display:flex;align-items:center;gap:16px;font-size:12px;line-height:15px;color:var(--ink)}
.fc-icon{width:28px;height:28px;border:1.5px solid var(--red);border-radius:6px;display:flex;align-items:center;justify-content:center}
.copyright{left:78px;top:262px;font-size:12px;color:var(--ink)}
.footer-links{right:78px;top:262px;font-size:12px;color:var(--ink)}
</style>
</head>
<body>

<header class="section site-header">
  <div class="abs brand">Bramblewood Quarry Advisors</div>
  <nav class="abs main-nav">
    <a class="active" href="#">Home</a>
    <a href="#">About Us</a>
    <a href="#">Consultants</a>
    <a href="#">Services</a>
    <a href="#">Contact us</a>
  </nav>
</header>

<section class="section hero">
  <div class="hero-photo" role="img" aria-label="Photo of a professional woman writing notes on a clipboard"></div>
  <div class="abs hero-box">
    <h1>Training and<br>individual coaching<br>to help business<br>professionals<br>and lawyers</h1>
  </div>
</section>

<section class="section about">
  <div class="abs accent-dot"></div>
  <h2 class="abs">Bramblewood Quarry Advisors</h2>
  <div class="abs about-copy">
    <p>Welcome to Bramblewood Quarry Advisors. We train and coach business professionals and lawyers on strategies and techniques to engage, inform, and persuade their readers. We teach our clients that precisely understanding their readers' concerns and motivations leads them to select the appropriate tone, to develop the most effective narrative, and to make the complicated judgments necessary for effective written communication.</p>
    <p>We tangibly improved the written product of business professionals and lawyers at corporations and elite law firms by tailoring our training and coaching to our client's particular objectives and characteristics. As educators, our training methodology</p>
  </div>
  <a class="abs btn btn-red" href="#">Know More</a>
  <div class="abs about-photo" role="img" aria-label="Photo of a trainer presenting to a small group of professionals in a meeting room"></div>
  <div class="abs ornament" role="img" aria-label="Decorative round dot pattern"></div>
</section>

<section class="section consultants">
  <h2 class="section-title">Our consultants</h2>

  <article class="abs card card-one">
    <div class="card-profile">
      <div class="portrait" role="img" aria-label="Portrait of consultant Maren Aldecott"></div>
      <div class="person">Maren Aldecott</div>
    </div>
    <div class="card-bio">
      <p>Maren Aldecott is an Associate Professor and Director of the Academic Enrichment Program at Halverston University School of Law. She has devoted her career in legal education to teaching and counseling students and attorneys, with a focus on developing the fundamental skills to promote success and wellbeing in law school and in the legal profession. Previously, she served as a Professor and Director of Academic Excellence, and most recently as Dean and Associate Dean at Eastbrook Law. She is a former member of the faculty at Carrow University Law School, a Visiting Professor at Wexley University, and a Teaching Fellow at Ashgrove College.</p>
      <a class="btn btn-white" href="#">know More</a>
    </div>
  </article>

  <article class="abs card card-two">
    <div class="card-bio">
      <p>Desmond Okafor provides legal and business writing consulting services to businesses, business professionals, law firms, and attorneys. He earned a Bachelor of Arts, cum laude, in English from Linford University, a Master of Fine Arts in creative writing from the Westmarch Writers' Workshop, and a Juris Doctor, cum laude, from Ashgrove Law School. At the University of Westmarch, Desmond served as the poetry editor of The Westmarch Review. At Ashgrove Law School, he served as treasurer and as an editor of the Ashgrove Law Review. Following graduation, Desmond practiced law at Pell &amp; Garrow L.L.P. (now Pell Marlowe) in Washington, D.C., then at Tindall, Rook &amp; Vance, L.L.P.</p>
      <a class="btn btn-white" href="#">know More</a>
    </div>
    <div class="card-profile">
      <div class="portrait" role="img" aria-label="Portrait of consultant Desmond Okafor"></div>
      <div class="person">Desmond Okafor</div>
    </div>
  </article>
</section>

<section class="section services">
  <h2 class="section-title">Our Services</h2>
  <p class="abs services-intro">The list below presents an overview of our services. We take pride in ensuring that our work<br>connects with each client's unique characteristics and its culture for written communications.</p>

  <article class="abs service s1">
    <div class="shot" style="height:288px;background:linear-gradient(160deg,#e9e7e2,#b9b4aa 50%,#4e4a45)" role="img" aria-label="Photo of a group of professionals working at a long table"></div>
    <h3>Training for twenty or<br>more professionals</h3>
    <p>Lorem ipsum dolor sit amet, consectetuer adipiscing elit. Aenean commodo ligula eget dolor. Aenean massa. Cum sociis natoque</p>
    <a class="btn btn-red" href="#">Know More</a>
  </article>

  <article class="abs service s2">
    <div class="shot" style="height:266px;background:linear-gradient(160deg,#5a3f2c,#8c6a4e 50%,#2d2622)" role="img" aria-label="Top-down photo of a team meeting around a wooden table with laptops"></div>
    <h3>Training for cohorts of up to<br>twenty professionals</h3>
    <p>Lorem ipsum dolor sit amet, consectetuer adipiscing elit. Aenean commodo ligula eget dolor. Aenean massa. Cum sociis natoque</p>
    <a class="btn btn-red" href="#">Know More</a>
  </article>

  <article class="abs service s3">
    <div class="shot" style="height:288px;background:linear-gradient(160deg,#f2f1ee,#c7c2b9 55%,#6a5a48)" role="img" aria-label="Photo of two people talking in armchairs in a bright office"></div>
    <h3>Training for cohorts followed<br>by one-hour individual<br>coaching for each participant</h3>
    <p>Lorem ipsum dolor sit amet, consectetuer adipiscing elit. Aenean commodo ligula eget</p>
    <a class="btn btn-red" href="#">Know More</a>
  </article>

  <article class="abs service s4">
    <div class="shot" style="height:288px;background:linear-gradient(160deg,#9a9ea3,#d6d3cf 50%,#3f4752)" role="img" aria-label="Photo of two colleagues reviewing notes together outdoors"></div>
    <h3>Individual coaching</h3>
    <p>Lorem ipsum dolor sit amet, consectetuer adipiscing elit. Aenean commodo ligula eget dolor. Aenean massa. Cum sociis natoque</p>
    <a class="btn btn-red" href="#">Know More</a>
  </article>
</section>

<section class="section contact">
  <div class="abs contact-band"></div>
  <h2 class="section-title">Contact Us</h2>
  <div class="abs contact-photo"><div role="img" aria-label="Photo of a woman working on a laptop at a desk"></div></div>
  <div class="abs field f-company">Company name</div>
  <div class="abs field f-contact">Contact name</div>
  <div class="abs field f-phone">phone number</div>
  <div class="abs field f-email">Email address</div>
  <div class="abs field f-address">Physical address</div>
  <div class="abs field f-message">Message</div>
  <a class="abs btn btn-red" href="#">Submit</a>
</section>

<footer class="section site-footer">
  <div class="abs footer-brand">Bramblewood Quarry Advisors</div>
  <div class="abs dotted" style="top:150px"></div>
  <div class="abs footer-contact">
    <div class="fc-item" style="left:210px">
      <span class="fc-icon"><svg width="14" height="14" viewBox="0 0 24 24"><path d="M6.6 10.8c1.4 2.8 3.8 5.1 6.6 6.6l2.2-2.2c.3-.3.7-.4 1-.2 1.1.4 2.3.6 3.6.6.6 0 1 .4 1 1V20c0 .6-.4 1-1 1C10.6 21 3 13.4 3 4c0-.6.4-1 1-1h3.5c.6 0 1 .4 1 1 0 1.3.2 2.5.6 3.6.1.3 0 .7-.2 1z" fill="none" stroke="#c8232d" stroke-width="2"/></svg></span>
      <span>CALL US<br>0147 258 3690</span>
    </div>
    <div class="fc-item" style="left:436px">
      <span class="fc-icon"><svg width="14" height="14" viewBox="0 0 24 24"><rect x="3" y="5" width="18" height="14" rx="2" fill="#c8232d"/><path d="M3 7l9 6 9-6" fill="none" stroke="#fff" stroke-width="1.8"/></svg></span>
      <span>EMAIL US<br>hello@bramblewoodquarry.com</span>
    </div>
    <div class="fc-item" style="left:722px">
      <span class="fc-icon"><svg width="14" height="14" viewBox="0 0 24 24"><path d="M12 2a7 7 0 0 0-7 7c0 5 7 13 7 13s7-8 7-13a7 7 0 0 0-7-7z" fill="#c8232d"/><circle cx="12" cy="9" r="2.6" fill="#fff"/></svg></span>
      <span>Address line Dummy Here<br>Address line Here</span>
    </div>
  </div>
  <div class="abs dotted" style="top:239px"></div>
  <div class="abs copyright">Copyright © 2024 All Rights Reserved By Company name</div>
  <div class="abs footer-links">Home | About Us | Consultants | Services | Contact Us</div>
</footer>

</body>
</html>
```